Restaurant Digital TV Menu Pictures

Need a digital menu board, image square of food. Something simple for customer to look and point to or say the food number. Image square 4x6, 5x7 or various of that. Vietnamese restaurant type food. I need template created and designer choice of design. Color scheme orange and white and little green. I would like to in the title of the food myself and written detail myself. I just need the template and possible have the design edit the picture a bit. Total food about 30 image will mostly be about 20-30 images. This will be display on a TV screen 16:9 size on a 55 inch tv. Attached is the food menu item. Also attach how the image off food will be taken. Also attach of other people design on the web. However, I would like number be label on the food item. I can find tune the correct information and food type and numbers later.

Font styles to use
Decorative

Colors
f37122
fffefb
9bcb3c

Requirements
Must have
• Photo edit food image basic making it pop. Make it look better, not magic, but better than my photography. Asian feel to the design.
Nice to have
• Fresh image of ingredients, (cilantro, freshly cook, non fast food) Image of green food

```html
<!DOCTYPE html>
<html lang="en">
<head>
<meta charset="utf-8">
<title>Lotus Lane Asian Kitchen – Digital Menu Board</title>
<link href="https://fonts.googleapis.com/css2?family=Luckiest+Guy&family=Oswald:wght@500&display=swap" rel="stylesheet">
<style>
  :root{
    --orange:#f37122;
    --orange-light:#fbb040;
    --orange-deep:#e8661c;
    --cream:#fffefb;
    --green:#1f7a1f;
    --green-bright:#9bcb3c;
    --price:#e0611a;
    --panel-head:#b84a12;
    --beef-dark:#3a2a20;
    --beef-mid:#7a4a2a;
    --popcorn-mid:#c9782e;
    --popcorn-light:#e8e2da;
  }
  *{box-sizing:border-box;margin:0;padding:0}
  html,body{width:1200px;height:786px;overflow:hidden}
  body{
    position:relative;
    background:
      radial-gradient(ellipse at 50% 40%, var(--orange-light) 0%, var(--orange) 55%, var(--orange-deep) 100%);
    font-family:"Luckiest Guy", cursive;
  }
  .brand{
    position:absolute;left:584px;top:0;width:185px;height:126px;
    background:var(--cream);
    display:flex;flex-direction:column;align-items:center;justify-content:center;gap:8px;
  }
  .brand-dot{width:44px;height:44px;border-radius:50%;background:var(--orange)}
  .brand-name{font-family:"Oswald",sans-serif;font-weight:500;font-size:13px;color:#444;letter-spacing:.5px}

  .menu-grid{
    position:absolute;left:23px;top:144px;
    display:grid;grid-template-columns:repeat(6,160px);grid-auto-rows:144px;
    column-gap:12px;row-gap:17px;
  }
  .dish-card{
    position:relative;background:var(--cream);
    border:1.5px solid var(--green);overflow:hidden;
    box-shadow:0 1px 3px rgba(0,0,0,.25);
  }
  .dish-title{
    position:absolute;left:0;top:4px;width:150px;height:32px;
    background:var(--green);border-radius:0 16px 16px 0;
    color:var(--cream);font-size:19px;line-height:34px;
    text-align:right;padding-right:14px;letter-spacing:.5px;
  }
  .dish-photo{
    position:absolute;right:4px;top:34px;width:98px;height:104px;
    border-radius:50% 50% 46% 46%;
  }
  .beef .dish-photo{background:radial-gradient(circle at 60% 55%, var(--beef-mid) 0%, var(--beef-dark) 70%, #111 100%)}
  .popcorn .dish-photo{background:radial-gradient(circle at 55% 50%, var(--popcorn-mid) 0%, #b0652a 55%, var(--popcorn-light) 78%)}
  .dish-desc{
    position:absolute;left:6px;top:40px;width:50px;
    font-family:"Oswald",sans-serif;font-size:5.2px;line-height:6.4px;
    color:var(--green);text-transform:uppercase;
  }
  .dish-price{
    position:absolute;left:6px;bottom:6px;
    color:var(--price);font-size:22px;line-height:1;
  }

  .side-panel{
    position:absolute;left:1058px;top:140px;width:128px;height:626px;
    background:var(--cream);border:3px solid var(--panel-head);
  }
  .side-panel h2{
    background:var(--panel-head);color:var(--cream);
    font-weight:400;font-size:21px;line-height:40px;text-align:center;letter-spacing:.5px;
  }
</style>
</head>
<body>
  <header class="brand">
    <span class="brand-dot"></span>
    <span class="brand-name">Lotus Lane Asian Kitchen</span>
  </header>

  <main class="menu-grid">
    <!-- row 1 -->
    <article class="dish-card beef"><h3 class="dish-title">Beef Rice</h3><p class="dish-desc">Grilled lemongrass beef on jasmine rice with slaw, egg roll and dipping sauce.</p><div class="dish-photo" role="img" aria-label="Beef rice bowl photo"></div><span class="dish-price">$9.99</span></article>
    <article class="dish-card popcorn"><h3 class="dish-title">Pop Corn</h3><p class="dish-desc">Crispy bite-size chicken tossed with five spice, chili salt and fresh cilantro.</p><div class="dish-photo" role="img" aria-label="Popcorn chicken plate photo"></div><span class="dish-price">$6.99</span></article>
    <article class="dish-card beef"><h3 class="dish-title">Beef Rice</h3><p class="dish-desc">Grilled lemongrass beef on jasmine rice with slaw, egg roll and dipping sauce.</p><div class="dish-photo" role="img" aria-label="Beef rice bowl photo"></div><span class="dish-price">$9.99</span></article>
    <article class="dish-card popcorn"><h3 class="dish-title">Pop Corn</h3><p class="dish-desc">Crispy bite-size chicken tossed with five spice, chili salt and fresh cilantro.</p><div class="dish-photo" role="img" aria-label="Popcorn chicken plate photo"></div><span class="dish-price">$6.99</span></article>
    <article class="dish-card beef"><h3 class="dish-title">Beef Rice</h3><p class="dish-desc">Grilled lemongrass beef on jasmine rice with slaw, egg roll and dipping sauce.</p><div class="dish-photo" role="img" aria-label="Beef rice bowl photo"></div><span class="dish-price">$9.99</span></article>
    <article class="dish-card popcorn"><h3 class="dish-title">Pop Corn</h3><p class="dish-desc">Crispy bite-size chicken tossed with five spice, chili salt and fresh cilantro.</p><div class="dish-photo" role="img" aria-label="Popcorn chicken plate photo"></div><span class="dish-price">$6.99</span></article>
    <!-- row 2 -->
    <article class="dish-card beef"><h3 class="dish-title">Beef Rice</h3><p class="dish-desc">Grilled lemongrass beef on jasmine rice with slaw, egg roll and dipping sauce.</p><div class="dish-photo" role="img" aria-label="Beef rice bowl photo"></div><span class="dish-price">$9.99</span></article>
    <article class="dish-card popcorn"><h3 class="dish-title">Pop Corn</h3><p class="dish-desc">Crispy bite-size chicken tossed with five spice, chili salt and fresh cilantro.</p><div class="dish-photo" role="img" aria-label="Popcorn chicken plate photo"></div><span class="dish-price">$6.99</span></article>
    <article class="dish-card beef"><h3 class="dish-title">Beef Rice</h3><p class="dish-desc">Grilled lemongrass beef on jasmine rice with slaw, egg roll and dipping sauce.</p><div class="dish-photo" role="img" aria-label="Beef rice bowl photo"></div><span class="dish-price">$9.99</span></article>
    <article class="dish-card popcorn"><h3 class="dish-title">Pop Corn</h3><p class="dish-desc">Crispy bite-size chicken tossed with five spice, chili salt and fresh cilantro.</p><div class="dish-photo" role="img" aria-label="Popcorn chicken plate photo"></div><span class="dish-price">$6.99</span></article>
    <article class="dish-card beef"><h3 class="dish-title">Beef Rice</h3><p class="dish-desc">Grilled lemongrass beef on jasmine rice with slaw, egg roll and dipping sauce.</p><div class="dish-photo" role="img" aria-label="Beef rice bowl photo"></div><span class="dish-price">$9.99</span></article>
    <article class="dish-card popcorn"><h3 class="dish-title">Pop Corn</h3><p class="dish-desc">Crispy bite-size chicken tossed with five spice, chili salt and fresh cilantro.</p><div class="dish-photo" role="img" aria-label="Popcorn chicken plate photo"></div><span class="dish-price">$6.99</span></article>
    <!-- row 3 -->
    <article class="dish-card beef"><h3 class="dish-title">Beef Rice</h3><p class="dish-desc">Grilled lemongrass beef on jasmine rice with slaw, egg roll and dipping sauce.</p><div class="dish-photo" role="img" aria-label="Beef rice bowl photo"></div><span class="dish-price">$9.99</span></article>
    <article class="dish-card popcorn"><h3 class="dish-title">Pop Corn</h3><p class="dish-desc">Crispy bite-size chicken tossed with five spice, chili salt and fresh cilantro.</p><div class="dish-photo" role="img" aria-label="Popcorn chicken plate photo"></div><span class="dish-price">$6.99</span></article>
    <article class="dish-card beef"><h3 class="dish-title">Beef Rice</h3><p class="dish-desc">Grilled lemongrass beef on jasmine rice with slaw, egg roll and dipping sauce.</p><div class="dish-photo" role="img" aria-label="Beef rice bowl photo"></div><span class="dish-price">$9.99</span></article>
    <article class="dish-card popcorn"><h3 class="dish-title">Pop Corn</h3><p class="dish-desc">Crispy bite-size chicken tossed with five spice, chili salt and fresh cilantro.</p><div class="dish-photo" role="img" aria-label="Popcorn chicken plate photo"></div><span class="dish-price">$6.99</span></article>
    <article class="dish-card beef"><h3 class="dish-title">Beef Rice</h3><p class="dish-desc">Grilled lemongrass beef on jasmine rice with slaw, egg roll and dipping sauce.</p><div class="dish-photo" role="img" aria-label="Beef rice bowl photo"></div><span class="dish-price">$9.99</span></article>
    <article class="dish-card popcorn"><h3 class="dish-title">Pop Corn</h3><p class="dish-desc">Crispy bite-size chicken tossed with five spice, chili salt and fresh cilantro.</p><div class="dish-photo" role="img" aria-label="Popcorn chicken plate photo"></div><span class="dish-price">$6.99</span></article>
    <!-- row 4 -->
    <article class="dish-card beef"><h3 class="dish-title">Beef Rice</h3><p class="dish-desc">Grilled lemongrass beef on jasmine rice with slaw, egg roll and dipping sauce.</p><div class="dish-photo" role="img" aria-label="Beef rice bowl photo"></div><span class="dish-price">$9.99</span></article>
    <article class="dish-card popcorn"><h3 class="dish-title">Pop Corn</h3><p class="dish-desc">Crispy bite-size chicken tossed with five spice, chili salt and fresh cilantro.</p><div class="dish-photo" role="img" aria-label="Popcorn chicken plate photo"></div><span class="dish-price">$6.99</span></article>
    <article class="dish-card beef"><h3 class="dish-title">Beef Rice</h3><p class="dish-desc">Grilled lemongrass beef on jasmine rice with slaw, egg roll and dipping sauce.</p><div class="dish-photo" role="img" aria-label="Beef rice bowl photo"></div><span class="dish-price">$9.99</span></article>
    <article class="dish-card popcorn"><h3 class="dish-title">Pop Corn</h3><p class="dish-desc">Crispy bite-size chicken tossed with five spice, chili salt and fresh cilantro.</p><div class="dish-photo" role="img" aria-label="Popcorn chicken plate photo"></div><span class="dish-price">$6.99</span></article>
    <article class="dish-card beef"><h3 class="dish-title">Beef Rice</h3><p class="dish-desc">Grilled lemongrass beef on jasmine rice with slaw, egg roll and dipping sauce.</p><div class="dish-photo" role="img" aria-label="Beef rice bowl photo"></div><span class="dish-price">$9.99</span></article>
    <article class="dish-card popcorn"><h3 class="dish-title">Pop Corn</h3><p class="dish-desc">Crispy bite-size chicken tossed with five spice, chili salt and fresh cilantro.</p><div class="dish-photo" role="img" aria-label="Popcorn chicken plate photo"></div><span class="dish-price">$6.99</span></article>
  </main>

  <aside class="side-panel">
    <h2>Side Panel</h2>
  </aside>
</body>
</html>
```